Calendar Ad / Flyer

Our law firm needs a calendar ad to place in a local calendar.
THE DEADLINE IS THIS THURSDAY 06/28/2018.

Attached is the ad used in last years calendar. A few notes on this...
**. This is by no means the model to follow.
Please be creative and do what makes more sense marketing wise.
1. Need to update the color scheme which corresponds to the new website at morvanlegal.net
2. The "MORVAN LEGAL | STANDING FIRM FOR YOUR FUTURE" should be put at the top and made larger
3. "KNOWN AND TRUSTED IN OUR COMMUNITY FOR OVER 21 YEARS" should be changed to "KNOWN AND TRUSTED IN OUR COMMUNITY FOR OVER 22 YEARS"
4. "Dorian K. Morvan, Esq." should be made larger and better positioned.
5. Under the list of practices, it should be changed to have:
"Personal Injury, Legal Malpractice, Unlicensed Contractors, Medical Malpractice, Civil Litigation"
6. Contact information (i.e. contact number, website, and address) should be better positioned
7. Placement of endorsement logos should stand out more.
8. New picture of head attorney is attached.

Last but not least... Give it your best shot!

```html
<!DOCTYPE html>
<html lang="en">
<head>
<meta charset="utf-8">
<title>Morvan Legal – Calendar Ad</title>
<link href="https://fonts.googleapis.com/css2?family=Montserrat:wght@500;600&family=Open+Sans:wght@400&family=Tinos:wght@400&display=swap" rel="stylesheet">
<style>
  :root {
    --page: #e9eaec;
    --ink-dark: #2e2c2d;
    --ink-deep: #1f1e1f;
    --gold: #c6a673;
    --gold-light: #d9c3a0;
    --white: #ffffff;
    --list-text: #e2e2e2;
    --stripe: #a9a9ab;
    --stripe-light: #cfcfd1;
    --photo-warm: #8a6c55;
    --photo-cool: #c9c4bd;
    --photo-suit: #8d9096;
  }
  * { box-sizing: border-box; margin: 0; padding: 0; }
  html, body { width: 1200px; height: 910px; overflow: hidden; }
  body { background: var(--page); position: relative; }

  .ad {
    position: absolute; left: 100px; top: 80px;
    width: 1000px; height: 750px;
    background: var(--white);
    overflow: hidden;
  }
  .ad-backdrop { position: absolute; inset: 0; }
  .attorney-photo { position: absolute; inset: 0; }

  .brand {
    position: absolute; left: 28px; top: 94px;
    display: flex; align-items: center; gap: 14px;
  }
  .brand-mark { width: 34px; height: 34px; background: var(--gold); }
  .brand-name {
    font-family: "Montserrat", sans-serif; font-weight: 600;
    font-size: 40px; letter-spacing: 6px; color: var(--gold); line-height: 1;
  }
  .brand-tagline {
    position: absolute; left: 124px; top: 139px;
    font-family: "Montserrat", sans-serif; font-weight: 500;
    font-size: 13px; letter-spacing: 1.2px; color: var(--list-text);
  }

  .headline {
    position: absolute; left: 28px; top: 206px;
    font-family: "Tinos", serif; font-size: 24.5px; line-height: 31px;
    color: var(--white); text-transform: uppercase;
  }

  .attorney-name {
    position: absolute; left: 28px; top: 334px;
    font-family: "Tinos", serif; font-size: 37px; color: var(--white);
  }

  .practice-areas {
    position: absolute; left: 28px; top: 426px;
    display: grid; grid-template-columns: 242px 240px; row-gap: 5px;
    list-style: none;
    font-family: "Open Sans", sans-serif; font-size: 17.5px; color: var(--list-text);
  }
  .practice-areas li { display: flex; align-items: center; gap: 14px; height: 21px; }
  .practice-areas svg { flex: none; }

  .contact {
    position: absolute; left: 28px; top: 562px;
    font-family: "Open Sans", sans-serif; font-size: 18.5px; line-height: 28px;
  }
  .contact-line { color: var(--gold); }
  .contact-address { color: var(--white); }

  .endorsements {
    position: absolute; left: 0; top: 642px; width: 640px; height: 108px;
    display: flex; align-items: center; justify-content: space-around;
    padding: 0 14px;
  }
</style>
</head>
<body>
  <main class="ad">
    <svg class="ad-backdrop" width="1000" height="750" viewBox="0 0 1000 750" aria-hidden="true">
      <defs>
        <linearGradient id="panelShade" x1="0" y1="0" x2="1" y2="1">
          <stop offset="0" stop-color="#343233"/>
          <stop offset="1" stop-color="#262526"/>
        </linearGradient>
      </defs>
      <rect class="dark-panel" x="0" y="0" width="1000" height="642" fill="url(#panelShade)"/>
    </svg>

    <svg class="attorney-photo" width="1000" height="750" viewBox="0 0 1000 750" role="img" aria-label="Portrait photograph of the head attorney in a grey suit and blue tie, standing in a softly blurred office">
      <defs>
        <linearGradient id="photoTone" x1="0" y1="0" x2="1" y2="1">
          <stop offset="0" stop-color="var(--photo-warm)"/>
          <stop offset="0.45" stop-color="var(--photo-cool)"/>
          <stop offset="1" stop-color="var(--photo-suit)"/>
        </linearGradient>
      </defs>
      <polygon points="700,0 1000,0 1000,750 640,750 640,642 690,642 500,362" fill="url(#photoTone)"/>
      <polygon class="chevron-stripe" points="680,0 700,0 500,362 690,642 668,642 478,362" fill="var(--stripe)"/>
      <polygon class="chevron-stripe" points="640,0 660,0 460,362 650,642 628,642 438,362" fill="var(--stripe-light)" opacity="0.35"/>
      <polygon class="name-band" points="0,315 395,315 440,362 395,406 0,406" fill="var(--gold)"/>
      <polygon class="name-band-accent" points="420,315 445,315 490,362 445,406 420,406 465,362" fill="var(--gold-light)"/>
    </svg>

    <div class="brand">
      <span class="brand-mark"></span>
      <span class="brand-name">MORVAN LEGAL</span>
    </div>
    <p class="brand-tagline">STANDING FIRM FOR YOUR FUTURE</p>

    <h1 class="headline">Known and trusted in our<br>community for over 22 years</h1>

    <h2 class="attorney-name">Dorian K. Morvan, Esq.</h2>

    <ul class="practice-areas">
      <li><svg width="14" height="14" viewBox="0 0 14 14" aria-hidden="true"><circle cx="7" cy="7" r="7" fill="var(--gold)"/><path d="M5.5 4 L8.5 7 L5.5 10" stroke="var(--ink-dark)" stroke-width="2" fill="none"/></svg>Personal Injury</li>
      <li><svg width="14" height="14" viewBox="0 0 14 14" aria-hidden="true"><circle cx="7" cy="7" r="7" fill="var(--gold)"/><path d="M5.5 4 L8.5 7 L5.5 10" stroke="var(--ink-dark)" stroke-width="2" fill="none"/></svg>Civil Litigation</li>
      <li><svg width="14" height="14" viewBox="0 0 14 14" aria-hidden="true"><circle cx="7" cy="7" r="7" fill="var(--gold)"/><path d="M5.5 4 L8.5 7 L5.5 10" stroke="var(--ink-dark)" stroke-width="2" fill="none"/></svg>Legal Malpractice</li>
      <li><svg width="14" height="14" viewBox="0 0 14 14" aria-hidden="true"><circle cx="7" cy="7" r="7" fill="var(--gold)"/><path d="M5.5 4 L8.5 7 L5.5 10" stroke="var(--ink-dark)" stroke-width="2" fill="none"/></svg>Business LAw</li>
      <li><svg width="14" height="14" viewBox="0 0 14 14" aria-hidden="true"><circle cx="7" cy="7" r="7" fill="var(--gold)"/><path d="M5.5 4 L8.5 7 L5.5 10" stroke="var(--ink-dark)" stroke-width="2" fill="none"/></svg>Unlicensed Contractors,</li>
      <li><svg width="14" height="14" viewBox="0 0 14 14" aria-hidden="true"><circle cx="7" cy="7" r="7" fill="var(--gold)"/><path d="M5.5 4 L8.5 7 L5.5 10" stroke="var(--ink-dark)" stroke-width="2" fill="none"/></svg>Immigration Law</li>
      <li><svg width="14" height="14" viewBox="0 0 14 14" aria-hidden="true"><circle cx="7" cy="7" r="7" fill="var(--gold)"/><path d="M5.5 4 L8.5 7 L5.5 10" stroke="var(--ink-dark)" stroke-width="2" fill="none"/></svg>Medical Malpractice</li>
      <li><svg width="14" height="14" viewBox="0 0 14 14" aria-hidden="true"><circle cx="7" cy="7" r="7" fill="var(--gold)"/><path d="M5.5 4 L8.5 7 L5.5 10" stroke="var(--ink-dark)" stroke-width="2" fill="none"/></svg>Elder Abuse and Neglect</li>
    </ul>

    <address class="contact" style="font-style: normal;">
      <p class="contact-line">310.555.0148 &nbsp;|&nbsp; www.morvanlegal.net</p>
      <p class="contact-address">8120 Larkmont Ave., Suite #402 Beverly Hills, CA 90211</p>
    </address>

    <div class="endorsements" aria-label="Endorsements">
      <svg width="70" height="70" viewBox="0 0 70 70" aria-hidden="true"><circle cx="35" cy="35" r="33" fill="#7a1f1f"/></svg>
      <svg width="74" height="54" viewBox="0 0 74 54" aria-hidden="true"><rect width="74" height="54" fill="#c8262b"/></svg>
      <svg width="76" height="54" viewBox="0 0 76 54" aria-hidden="true"><rect width="76" height="54" rx="4" fill="#b89a5a"/></svg>
      <svg width="108" height="42" viewBox="0 0 108 42" aria-hidden="true"><rect width="108" height="42" rx="4" fill="#1d5f96"/></svg>
      <svg width="80" height="70" viewBox="0 0 80 70" aria-hidden="true"><circle cx="40" cy="33" r="30" fill="#2a8fd0"/></svg>
    </div>
  </main>
</body>
</html>
```